I have a business that exists already (Belvina Conservatory of Music) that we offer music lessons to all instruments. I recently opened a smaller version called TONES by Belvina that will only teach piano lessons. What I'm looking for now is a 3 page Website on word press. After I choose the design I like I want to be able to take over the website and bring it to our hosting company. We want full control of it and our team will take over. The reason I'm doing this is to have other visions and ideas from others. The first page will be about the company and our message/vision. Second page about the piano lessons. The third will be about franchising this concept "Tones by Belvina" Attached are 3 Logos . Please refer to our existing website www.belvinamusicschool-example.com to look at our piano page and franchising page. Please feel free to message me if you need more info. Thanks
Please note I do not want the new website (Tones by Belvina) To look like the other Website (Belvina Conservatory of Music) Fresh new look. I do not want the colours red or using the Red logo. I only provided it so that you have an Idea of What the other business looks like and that you can take the piano content and franchise content off of it. Tones by Belvina is smaller concept and only piano lessons.
Thanks
Only Piano lessons for all students
3 page

```html
<!DOCTYPE html>
<html lang="en">
<head>
<meta charset="utf-8">
<title>Tones by Belvina — Piano Lessons</title>
<link href="https://fonts.googleapis.com/css2?family=Cinzel:wght@400;500&family=Lora:ital,wght@0,400;1,400&family=Mulish:wght@400;500&display=swap" rel="stylesheet">
<style>
  :root{
    --blue:#2a9af0;
    --teal:#4ec4bf;
    --ink:#1d1d1d;
    --text:#444;
    --muted:#6b6b6b;
    --line:#e3e3e3;
    --dark-band:#2b2b2b;
    --footer:#000;
    --white:#fff;
  }
  *{box-sizing:border-box;margin:0;padding:0}
  html,body{width:1200px;height:2812px;overflow:hidden;background:var(--white)}
  body{position:relative;font-family:"Mulish",sans-serif;color:var(--text)}
  .abs{position:absolute}
  .center{left:0;width:1200px;text-align:center}

  /* header */
  .site-header{left:0;top:0;width:1200px;height:85px;background:var(--white)}
  .brand{left:142px;top:14px;font-family:"Cinzel",serif;font-size:30px;color:var(--ink);letter-spacing:1px;line-height:40px}
  .brand-mark{display:inline-block;width:14px;height:14px;background:var(--ink);margin-right:8px;vertical-align:middle}
  .brand-sub{left:180px;top:50px;font-family:"Cinzel",serif;font-size:13px;color:var(--ink)}
  .nav{right:140px;top:29px;display:flex;gap:35px;font-family:"Lora",serif;font-size:13px;letter-spacing:1.2px;color:var(--ink)}
  .nav .active{color:var(--blue)}

  /* hero */
  .hero{left:0;top:85px;width:1200px;height:480px;background:linear-gradient(90deg,#c9b29a 0%,#e8e4e0 30%,#f2f0ef 55%,#ebe8e6 100%)}
  .hero-copy{right:144px;top:130px;text-align:right;font-family:"Cinzel",serif;color:var(--ink)}
  .hero-copy .l1{font-size:30px;line-height:40px}
  .hero-copy .l2{font-size:46px;line-height:54px;letter-spacing:1px}
  .hero-copy .l3{font-size:30px;line-height:40px}
  .btn{display:inline-block;background:var(--blue);color:var(--white);font-family:"Cinzel",serif;text-align:center}
  .hero .btn{position:absolute;right:142px;top:290px;width:182px;height:35px;line-height:35px;font-size:17px;box-shadow:0 2px 6px rgba(0,0,0,.15)}

  /* about */
  .section-title{font-family:"Lora",serif;font-size:32px;letter-spacing:1px}
  .about-title{top:622px}
  .about-title .blue{color:var(--blue)}
  .about-title .logo-word{color:var(--ink);font-family:"Cinzel",serif;margin-left:10px;font-size:30px}
  .title-rule{height:3px;width:126px;left:537px;background:linear-gradient(90deg,var(--blue) 50%,var(--ink) 50%)}
  .intro{top:684px;left:190px;width:820px;text-align:center;font-size:14px;line-height:25px;color:var(--text)}

  .frame-grey{background:#e6e6e6}
  .photo{}
  .feature-heading{left:592px;top:804px;font-family:"Lora",serif;font-style:italic;font-size:31px;color:var(--blue)}
  .feature-text{left:592px;top:857px;width:470px;font-size:14px;line-height:25.5px;color:var(--text)}
  .feature-text p+p{margin-top:6px}
  .read-more{left:592px;top:1024px;width:155px;height:35px;line-height:35px;font-size:16px}

  /* vision */
  .vision{left:0;top:1140px;width:1200px;height:341px;background:linear-gradient(160deg,#3a3a3a 0%,#262626 55%,#1d1d1d 100%)}
  .vision-title{top:55px;color:var(--white);font-family:"Lora",serif;font-size:32px;letter-spacing:1px}
  .vision .title-rule{top:107px}
  .vision-text{left:220px;top:128px;width:760px;text-align:center;color:#eee;font-size:14px;line-height:25.5px}
  .vision .btn{position:absolute;left:509px;top:225px;width:182px;height:34px;line-height:34px;font-size:17px}

  /* programs */
  .programs-head{left:142px;top:1553px;height:48px;border-left:5px solid var(--ink);padding-left:13px;font-family:"Lora",serif;font-size:19px;line-height:24px;color:var(--blue)}
  .programs-photo{left:142px;top:1623px;width:344px;height:315px;border:7px solid var(--blue);background:linear-gradient(135deg,#e9e9e9,#cfcac4 60%,#b9b2aa)}
  .card{width:268px;height:91px;background:var(--white);box-shadow:0 0 6px rgba(0,0,0,.12);padding:14px 12px 0 12px}
  .card p{border-left:3px solid var(--blue);padding-left:9px;font-size:13px;line-height:18.5px;color:var(--text);min-height:40px}

  /* quote */
  .quote-card{left:142px;top:2115px;width:915px;height:210px;background:var(--white);border-radius:14px;box-shadow:0 0 14px rgba(0,0,0,.1)}
  .quote-marks{left:225px;top:2118px;font-family:"Lora",serif;font-size:170px;color:#eaeaea;line-height:1}
  .quote-text{left:270px;top:2162px;width:660px;text-align:center;font-family:"Lora",serif;font-style:italic;font-size:23px;line-height:38px;color:var(--ink)}
  .quote-author{top:2250px;font-family:"Lora",serif;font-size:18px;color:var(--teal);letter-spacing:.5px}

  /* franchise */
  .note-deco{left:110px;top:2380px;width:95px;height:155px;background:linear-gradient(180deg,#f2f2f2,#e9e9e9);border-radius:40px 40px 40px 40px;opacity:.7}
  .franchise-title{top:2392px;font-family:"Lora",serif;font-size:46px;color:var(--ink)}
  .franchise-sub{top:2462px;font-family:"Lora",serif;font-size:20px;color:var(--ink);letter-spacing:.5px}
  .know-more{left:530px;top:2507px;width:140px;height:34px;line-height:34px;background:var(--teal);color:var(--white);text-align:center;font-family:"Lora",serif;font-size:12px;letter-spacing:1px}

  /* footer */
  .site-footer{left:0;top:2613px;width:1200px;height:150px;background:var(--footer);color:var(--white)}
  .contact{display:flex;align-items:center;gap:12px;position:absolute;top:0;height:150px}
  .icon-ring{width:38px;height:38px;border:2.5px solid var(--white);border-radius:50%;display:flex;align-items:center;justify-content:center}
  .contact .label{font-family:"Lora",serif;font-size:14px;line-height:18px}
  .contact .big{font-family:"Lora",serif;font-size:20px;line-height:24px}
  .contact .small{font-family:"Lora",serif;font-size:12.5px;line-height:19px}
  .contact .strong{font-family:"Lora",serif;font-size:14px;line-height:19px;letter-spacing:.5px}
  .divider{position:absolute;top:62px;width:1px;height:26px;background:#555}
  .copyright-bar{left:0;top:2763px;width:1200px;height:49px;background:var(--teal)}
  .copyright{left:142px;top:16px;font-size:13px;color:var(--white)}
  .social{position:absolute;top:12px;right:140px;display:flex;gap:8px}
  .social span{width:25px;height:25px;border:1.5px solid var(--white);border-radius:50%}
</style>
</head>
<body>

<header class="abs site-header">
  <div class="abs brand"><span class="brand-mark"></span>TONES</div>
  <div class="abs brand-sub">by Belvina</div>
  <nav class="abs nav">
    <span class="active">HOME</span>
    <span>PIANO LESSONS</span>
    <span>FRANCHISING</span>
    <span>CONTACT US</span>
  </nav>
</header>

<section class="abs hero">
  <div class="abs" role="img" aria-label="Teacher and young student playing a white grand piano in a bright room" style="left:0;top:0;width:560px;height:480px;background:linear-gradient(90deg,#b9a48f,#d8cfc6 70%,rgba(236,233,230,0))"></div>
  <div class="abs" style="left:950px;top:0;width:1px;height:480px;background:#555"></div>
  <div class="abs hero-copy">
    <div class="l1">We Provide</div>
    <div class="l2">PIANO LESSONS</div>
    <div class="l3">For All Students</div>
  </div>
  <span class="btn">Contact Us Today</span>
</section>

<h2 class="abs center section-title about-title"><span class="blue">ABOUT</span><span class="logo-word">TONES by Belvina</span></h2>
<div class="abs title-rule" style="top:671px"></div>
<p class="abs intro">Lorem hendrerit in vulputate velit esse molestie consequat, velocity illum dolore eu feugiat nulla facilisis at vero eros et accumsan etlict iusto odio dignissim qui blandit praesent luptatum zzril delenit loei augue duis dolore te feugait nulla facilisi.</p>

<div class="abs frame-grey" style="left:240px;top:778px;width:230px;height:264px"></div>
<div class="abs" style="left:262px;top:800px;width:186px;height:220px;background:var(--white)"></div>
<div class="abs frame-grey" style="left:300px;top:1050px;width:275px;height:28px"></div>
<div class="abs" role="img" aria-label="Students playing piano and strings together in a rehearsal room" style="left:142px;top:755px;width:273px;height:243px;background:linear-gradient(135deg,#5a4a3c,#a07a5a 55%,#d8b796)"></div>
<div class="abs" role="img" aria-label="Black grand piano on a stage in front of a brick wall" style="left:293px;top:826px;width:274px;height:243px;background:linear-gradient(180deg,#e4e0da 0%,#c9c4bc 50%,#4d6a8a 78%,#8a6a42 100%)"></div>

<h3 class="abs feature-heading">Playing the Piano</h3>
<div class="abs feature-text">
  <p>When you think of a piano, you probably envision black and white keys but the piano is more than those harmonious sounds created by the player. The versatility and the musicianship instilled into the player from those keys is the true magic that comes from playing piano!</p>
  <p>Starting from the grassroots, experience different methods and styles of playing piano.</p>
</div>
<span class="abs btn read-more">Read More</span>

<section class="abs vision">
  <div class="abs" role="img" aria-label="Close-up of piano keys in dark monochrome" style="left:0;top:0;width:1200px;height:341px;background:linear-gradient(170deg,rgba(90,90,90,.35) 0%,rgba(60,60,60,.2) 40%,rgba(120,120,120,.25) 100%)"></div>
  <h2 class="abs center vision-title">OUR VISION</h2>
  <div class="title-rule abs"></div>
  <p class="abs vision-text">Our Mission is Lorem ipsum dolor sit amet, consectetuer adipiscig elit, sed diama nonummy nibh euismod tincidunt ut laoreet dolore magna aliquam erat volutpat. Ut wisi enim ad minim veniam. Lorem hendrerit in vulputate velit esse molestie consequat, velocity illum dolore eu feugiat nulla facilisis at vero eros.</p>
  <span class="btn">Contact Us Today</span>
</section>

<h3 class="abs programs-head">OUR PROGRAMS ALSO PROVIDE<br>STUDENTS THE OPPORTUNITY TO:</h3>
<div class="abs programs-photo" role="img" aria-label="Students practising on digital pianos in a bright classroom"></div>

<div class="abs card" style="left:513px;top:1626px"><p>Participate in large-scale performances.</p></div>
<div class="abs card" style="left:792px;top:1626px"><p>Perform at Belvina’s many community events on a regular basis.</p></div>
<div class="abs card" style="left:513px;top:1732px"><p>Access the GTA’s coolest Broadcast stage</p></div>
<div class="abs card" style="left:792px;top:1732px"><p>Attend Clinics, Masterclasses, and Jam Nights</p></div>
<div class="abs card" style="left:513px;top:1838px"><p>Access the Belvina Rocks band program. Belvina’s Band Program empowers.</p></div>
<div class="abs card" style="left:792px;top:1838px"><p>Register in our elite teaching program to learn how to pass on the magic.</p></div>

<div class="abs quote-card"></div>
<div class="abs quote-marks">“</div>
<p class="abs quote-text">“Life is like a piano. What you get out of it depends on how you play it.”</p>
<div class="abs center quote-author">THEO MARLOWE</div>

<div class="abs note-deco" role="img" aria-label="Faint musical note decoration"></div>
<h2 class="abs center franchise-title">Franchise Opportunities</h2>
<p class="abs center franchise-sub">BE PART OF THE BELVINA ACADEMY FAMILY</p>
<span class="abs know-more">KNOW MORE</span>

<footer class="abs site-footer">
  <div class="contact" style="left:190px">
    <span class="icon-ring">
      <svg width="18" height="18" viewBox="0 0 24 24" fill="#fff"><path d="M6.6 10.8a15 15 0 0 0 6.6 6.6l2.2-2.2c.3-.3.7-.4 1-.2 1.1.4 2.3.6 3.6.6.6 0 1 .4 1 1V20c0 .6-.4 1-1 1A17 17 0 0 1 3 4c0-.6.4-1 1-1h3.5c.6 0 1 .4 1 1 0 1.3.2 2.5.6 3.6.1.3 0 .7-.2 1z"/></svg>
    </span>
    <div><div class="label">Call Us Now</div><div class="big">1-800-555-0142</div></div>
  </div>
  <div class="divider" style="left:442px"></div>
  <div class="contact" style="left:479px">
    <span class="icon-ring">
      <svg width="16" height="20" viewBox="0 0 16 20" fill="none" stroke="#fff" stroke-width="2"><path d="M8 19s6-6.2 6-11A6 6 0 0 0 2 8c0 4.8 6 11 6 11z"/><circle cx="8" cy="8" r="2.2"/></svg>
    </span>
    <div><div class="strong">TONES BELVINA</div><div class="small">123, Building Name, Street Name<br>State, City XY 123456</div></div>
  </div>
  <div class="divider" style="left:757px"></div>
  <div class="contact" style="left:814px">
    <span class="icon-ring">
      <svg width="18" height="14" viewBox="0 0 18 14" fill="#fff"><rect x="0" y="0" width="18" height="14" rx="2"/><path d="M1 1.5l8 6 8-6" fill="none" stroke="#000" stroke-width="1.6"/></svg>
    </span>
    <div><div class="label">Email Us:</div><div class="small">hello@tonesbelvina-example.com</div></div>
  </div>
</footer>

<div class="abs copyright-bar">
  <p class="abs copyright">Copyright © 2020 TONES BELVINA. All Rights Reserved.</p>
  <div class="social"><span></span><span></span><span></span><span></span></div>
</div>

</body>
</html>
```